Boutique Recruiting Firm Needs Eye-Catching Business Cards (and potentially new logo)!

I run a recruiting company in Charleston, South Carolina. I have a ton of networking events coming up and need business cards to grab potential clients attention.

I currently have a logo but if you want to try and recreate the logo to something more modern I am open to that. If you do decide to create a new logo please submit the business card with the old logo and the new one.

Staffing Under Blue Lanterns, LLC is the name of my company. I create videos to my clients and candidates which allows me to standout from my competition so I would like a business card (and possibly new logo) to do the same.

I do not specialize in any one industry of recruiting.

```html
<!DOCTYPE html>
<html lang="en">
<head>
<meta charset="utf-8">
<title>Staffing Under Blue Lanterns, LLC — Business Card</title>
<link href="https://fonts.googleapis.com/css2?family=Open+Sans:wght@400;600;700&display=swap" rel="stylesheet">
<style>
  :root {
    --backdrop: #e7e3df;
    --card: #f4f4f4;
    --card-edge: #dcdcdc;
    --ink: #1e1e1e;
    --ink-soft: #2c2c2c;
    --divider: #cfcfcf;
  }
  * { box-sizing: border-box; margin: 0; padding: 0; }
  html, body { width: 1200px; height: 1000px; overflow: hidden; }
  body {
    background: var(--backdrop);
    font-family: "Open Sans", Arial, sans-serif;
    color: var(--ink);
  }
  .canvas { position: relative; width: 1200px; height: 1000px; overflow: hidden; }

  .card {
    position: absolute;
    left: 265px;
    width: 666px;
    height: 397px;
    background: var(--card);
    border: 1px solid var(--card-edge);
    box-shadow: 0 6px 14px rgba(0, 0, 0, 0.12);
  }
  .card--front { top: 73px; }
  .card--back { top: 532px; }

  .brand {
    position: absolute;
    display: flex;
    align-items: center;
    transform: translate(-50%, -50%);
    white-space: nowrap;
  }
  .brand__mark {
    flex: none;
    background: var(--ink);
  }
  .brand__name {
    font-weight: 700;
    color: var(--ink);
    text-transform: uppercase;
    letter-spacing: 0.02em;
  }
  .card--front .brand { left: 333px; top: 198px; gap: 18px; }
  .card--front .brand__mark { width: 42px; height: 42px; }
  .card--front .brand__name { font-size: 34px; line-height: 39px; }
  .card--back .brand { left: 186px; top: 198px; gap: 14px; }
  .card--back .brand__mark { width: 32px; height: 32px; }
  .card--back .brand__name { font-size: 26px; line-height: 30px; }

  .divider {
    position: absolute;
    left: 371px; top: 70px;
    width: 1px; height: 260px;
    background: linear-gradient(to bottom, transparent, var(--divider) 20%, var(--divider) 80%, transparent);
  }

  .contact {
    position: absolute;
    left: 410px; top: 98px;
    color: var(--ink-soft);
  }
  .contact__name { font-size: 21px; font-weight: 600; color: var(--ink); line-height: 1.2; }
  .contact__role { font-size: 16px; line-height: 1.3; margin-bottom: 24px; }
  .contact__address { font-size: 16px; line-height: 21px; font-style: normal; margin-bottom: 13px; }
  .contact__list { list-style: none; font-size: 16px; line-height: 23px; }
  .contact__list li { display: flex; align-items: center; gap: 7px; }
  .contact__list svg { width: 16px; height: 16px; flex: none; fill: var(--ink); }
</style>
</head>
<body>
<main class="canvas">

  <section class="card card--front">
    <div class="brand">
      <span class="brand__mark"></span>
      <p class="brand__name">Staffing<br>Under Blue<br>Lanterns, LLC</p>
    </div>
  </section>

  <section class="card card--back">
    <div class="brand">
      <span class="brand__mark"></span>
      <p class="brand__name">Staffing<br>Under Blue<br>Lanterns, LLC</p>
    </div>
    <div class="divider"></div>
    <div class="contact">
      <p class="contact__name">Dorian Vell</p>
      <p class="contact__role">Film Operation</p>
      <address class="contact__address">Level 12, 40 Harbor Court<br>Marlow Bay, Eastshore</address>
      <ul class="contact__list">
        <li>
          <svg viewBox="0 0 16 16" aria-hidden="true"><path d="M2 6c0-2 2.5-3.5 6-3.5S14 4 14 6v1h-3V5.5H5V7H2zM4 8h8l1.5 5h-11zM6.5 9.5a1.5 1.5 0 1 0 3 0 1.5 1.5 0 1 0-3 0z"/></svg>
          + 000 000 0000
        </li>
        <li>
          <svg viewBox="0 0 16 16" aria-hidden="true"><path d="M2 4h12v8H2zM3 5v.4l5 3.4 5-3.4V5z"/></svg>
          info@staffingubl.com
        </li>
        <li>
          <svg viewBox="0 0 16 16" aria-hidden="true"><path d="M6.6 9.4l2.8-2.8 1 1-2.8 2.8zM4.5 9.5l1.4-1.4 1 1-1.4 1.4a1 1 0 0 0 1.4 1.4l1.4-1.4 1 1-1.4 1.4a2.4 2.4 0 0 1-3.4-3.4zM11.5 6.5l-1.4 1.4-1-1 1.4-1.4a1 1 0 0 0-1.4-1.4L7.7 5.5l-1-1 1.4-1.4a2.4 2.4 0 0 1 3.4 3.4z"/></svg>
          www.staffingubl.com
        </li>
      </ul>
    </div>
  </section>

</main>
</body>
</html>
```